Corwick Roof Company need Flier for Department of Tillage

We need a 2 page flier for distributing to Military Contractors and Department of Tillage. We install residential solar and this will be used for military base housing and other gov. projects on the residential home communities. We need to show how large of a company we are and how we are able to work with the military //gov. projects. Attached is our website and other marketing info for your use. Thanks and good luck!

Target Market(s)

Military and Government Contractors //Department of Tillage

Industry/Entity Type

Solar Energy

Requirements
Must have
• Our Why - Statement included

```html
<!DOCTYPE html>
<html lang="en">
<head>
<meta charset="utf-8">
<title>Corwick Roof Company – Solar Flier</title>
<link href="https://fonts.googleapis.com/css2?family=Fira+Sans:ital,wght@0,400;0,500;0,600;0,700;1,600&family=Open+Sans:wght@400;600&family=Oswald:wght@700&display=swap" rel="stylesheet">
<style>
:root{
  --stage:#4a4a4c;
  --blue:#1a8fd6;
  --blue-dark:#1b75bb;
  --navy:#14457e;
  --green:#8cc63f;
  --green-dark:#5fa127;
  --orange:#f7941d;
  --cream:#fdfbe6;
  --ink:#1e1e1e;
  --grey-text:#555;
  --card:#ffffff;
}
*{margin:0;padding:0;box-sizing:border-box}
html,body{width:1200px;height:809px;overflow:hidden;background:var(--stage)}
body{position:relative;font-family:"Open Sans",sans-serif}
.page{position:absolute;top:59px;width:545px;height:707px;overflow:hidden;box-shadow:4px 6px 10px rgba(0,0,0,.45)}
.page-left{left:38px;background:var(--green)}
.page-right{left:610px;background:#fff}
.abs{position:absolute}
.head{font-family:"Fira Sans",sans-serif}

/* left page */
.hero{left:0;top:0;width:545px;height:157px;background:var(--cream)}
.hero-photo{left:0;top:0;width:240px;height:157px;background:linear-gradient(90deg,#8a4a2a 0%,#d9864a 45%,#f6d8a0 80%,rgba(253,251,230,0) 100%)}
.hero-title{left:117px;top:20px;font-size:24px;font-weight:600;color:var(--blue-dark);white-space:nowrap}
.hero-sub{right:25px;top:60px;font-size:13px;font-weight:600;color:var(--ink);white-space:nowrap}
.hero-sub .dot{display:inline-block;width:8px;height:8px;border-radius:50%;background:var(--orange);margin:0 6px;vertical-align:1px}
.hero-url{right:25px;top:120px;font-size:21px;font-weight:600;color:var(--blue-dark);letter-spacing:.5px}
.install{left:26px;top:175px;width:190px;color:#fff;font-weight:600;line-height:1.35;text-shadow:0 1px 2px rgba(0,0,0,.25)}
.install .big{font-size:21px;display:block;margin-bottom:4px}
.install .mid{font-size:15px}
.install .sm{font-size:12px}
.divider{left:222px;top:182px;width:1px;height:148px;background:rgba(255,255,255,.6)}
.why{left:244px;top:178px;width:278px;color:#fff;font-size:7.5px;line-height:1.45;text-align:justify}
.why p{margin-bottom:9px}
.card{top:353px;height:128px;background:var(--card);box-shadow:0 2px 3px rgba(0,0,0,.2);padding:7px 6px}
.card h3{font-family:"Fira Sans",sans-serif;font-weight:600;font-size:13px;line-height:1.2;color:var(--blue-dark)}
.card p{font-size:7.3px;color:var(--grey-text);line-height:1.35;margin-top:5px}
.card svg{position:absolute}
.quotes{left:0;top:493px;width:545px;height:108px;background:var(--blue-dark)}
.quotes-title{left:28px;top:10px;font-size:17px;font-weight:600;font-style:italic;color:#fff}
.quotes-rule{left:219px;top:23px;width:298px;height:3px;background:var(--orange)}
.quote{top:40px;width:128px;color:#fff;font-size:7.3px;line-height:1.35;text-align:justify}
.quote .who{display:block;text-align:right;font-weight:600;margin-top:8px}
.photo{top:601px;height:106px}

/* right page */
.title{left:34px;top:22px;font-family:"Oswald",sans-serif;font-size:44px;font-weight:700;color:var(--navy);letter-spacing:.5px;line-height:1}
.subtitle{left:34px;top:75px;font-size:18px;font-weight:600;color:var(--ink)}
.badge{left:26px;top:245px;width:144px;height:144px;border-radius:50%;background:var(--blue);border:5px solid #fff;box-shadow:0 2px 6px rgba(0,0,0,.3);display:flex;align-items:center;justify-content:center;text-align:center;color:#fff;font-size:18px;font-weight:600;line-height:1.05}
.logo{left:350px;top:221px;width:144px;height:144px;border-radius:50%;background:#fff;border:7px solid var(--orange);box-shadow:0 2px 6px rgba(0,0,0,.3);display:flex;align-items:center;justify-content:center;text-align:center;color:var(--blue-dark);font-size:17px;font-weight:600;line-height:1.15}
.easy{left:0;width:547px;top:390px;text-align:center;font-size:21px;font-weight:600;color:var(--blue-dark)}
.step{top:425px;height:144px;background:#f6f7f8;text-align:center;padding:0 4px}
.step svg{margin-top:8px}
.step h4{font-family:"Fira Sans",sans-serif;font-size:11.5px;font-weight:600;color:var(--blue-dark);line-height:1.2;margin-top:3px}
.step p{font-size:7.6px;color:var(--grey-text);line-height:1.35;margin-top:6px}
.tagline{left:26px;top:587px;font-size:20px;font-weight:600;color:var(--orange);white-space:nowrap}
.site{left:26px;top:621px;font-size:22px;font-weight:600;color:#333;letter-spacing:.6px}
.quote-cta{right:28px;color:#fff;text-align:right;font-family:"Fira Sans",sans-serif}
</style>
</head>
<body>

<!-- Page 1 -->
<section class="page page-left">
  <header class="abs hero">
    <div class="abs hero-photo" role="img" aria-label="Photo of a family silhouetted against a sunset, child on a parent's shoulders"></div>
    <h1 class="abs head hero-title">Bringing the Power of the SUN for you</h1>
    <p class="abs head hero-sub">Zero upfront Cost<span class="dot"></span>Lower monthly Energy Costs</p>
    <p class="abs head hero-url">www.CorwickRoof.com</p>
  </header>

  <div class="abs head install">
    <span class="big">We install</span>
    <span class="mid">Residential Solar</span><br>
    <span class="sm">and this will be used </span><span class="mid">For</span><br>
    <span class="mid">Military base housing</span><br>
    <span class="sm">and other </span><span class="mid">govt. projects</span><br>
    <span class="sm">on the Residential Home</span><br>
    <span class="sm">Communities.</span>
  </div>
  <div class="abs divider"></div>
  <div class="abs why">
    <p>We are on a mission to empower home owners and businesses to power their lives with better, less expensive, cleaner energy creating a world that is powered by the sun.</p>
    <p>With solar, homeowners are saving money while dramatically lessening the amount of pollution released into the atmosphere. We believe that, together, we can create a planet run by the sun.</p>
    <p>Everyone should have the freedom to choose where they get their energy and be able to control their energy costs. Homeowners across the nation rely on us to provide $0 upfront cost options in upgrading their home to solar energy in a way that saves them money on monthly electrical costs.</p>
    <p>Smart and forward thinking, Solar allows you the ability to lower your energy bills and avoid the costly rate increases.</p>
  </div>

  <article class="abs card" style="left:26px;width:114px">
    <h3>Reduce Energy</h3>
    <p>Protect your organization from rising energy prices.</p>
    <svg style="left:14px;top:58px" width="92" height="64" viewBox="0 0 92 64" font-family="Open Sans,sans-serif" font-size="7">
      <rect x="0" y="2" width="48" height="60" fill="#9aa5b1"/>
      <text x="24" y="36" fill="#fff" text-anchor="middle">Utility</text>
      <text x="24" y="45" fill="#fff" text-anchor="middle">Price</text>
      <rect x="52" y="34" width="40" height="28" fill="#8cc63f"/>
      <text x="72" y="46" fill="#fff" text-anchor="middle">SOLAR</text>
      <text x="72" y="55" fill="#fff" text-anchor="middle">Price</text>
      <polygon points="52,0 92,0 92,16 72,26 52,16" fill="#5fa127"/>
      <text x="72" y="12" fill="#fff" text-anchor="middle" font-weight="600" font-size="8">SAVE</text>
    </svg>
  </article>
  <article class="abs card" style="left:153px;width:116px">
    <h3>Savings Beyond Solar</h3>
    <p style="width:72px">SunHarbor energy efficiency solutions help you use less energy and save money</p>
    <p style="color:#5fa127;font-weight:600;font-size:7.5px;margin-top:5px">Energy Efficiency</p>
    <svg style="left:80px;top:44px" width="30" height="56" viewBox="0 0 30 56">
      <circle cx="15" cy="16" r="14" fill="#8cc63f"/>
      <text x="15" y="23" text-anchor="middle" font-family="Fira Sans,sans-serif" font-weight="700" font-size="20" fill="#14457e">$</text>
      <rect x="9" y="31" width="12" height="10" rx="2" fill="#8a9199"/>
    </svg>
  </article>
  <article class="abs card" style="left:281px;width:114px">
    <h3>What Will Electricity Cost?</h3>
    <p>SunHarbor makes it easy and affordable to save with solar.</p>
    <svg style="left:6px;top:72px" width="102" height="50" viewBox="0 0 102 50" font-family="Open Sans,sans-serif" font-size="4.5">
      <polygon points="0,38 102,8 102,40 0,40" fill="#9aa5b1"/>
      <polygon points="0,40 102,34 102,40" fill="#8cc63f"/>
      <text x="20" y="30" transform="rotate(-16 20 30)" fill="#333">Utility Bill Without Solar</text>
      <text x="50" y="39" fill="#333" text-anchor="middle">Utility Bill Without Solar</text>
      <line x1="0" y1="41" x2="102" y2="41" stroke="#666" stroke-width=".5"/>
      <text x="0" y="48">Year 1</text><text x="30" y="48">Year 10</text><text x="80" y="48">Year 20</text>
    </svg>
  </article>
  <article class="abs card" style="left:406px;width:115px">
    <h3>Energy Monitoring</h3>
    <p>WattTrackTM tracks your solar production and electricity consumption</p>
    <svg style="left:6px;top:80px" width="104" height="28" viewBox="0 0 104 28">
      <rect width="104" height="28" fill="#eceae6"/>
      <path d="M0,20 L12,12 L24,18 L38,8 L52,16 L68,10 L84,18 L104,12 L104,28 L0,28Z" fill="#c7bfb6"/>
      <g fill="#5fa127">
        <rect x="36" y="20" width="2" height="8"/><rect x="40" y="16" width="2" height="12"/><rect x="44" y="12" width="2" height="16"/>
        <rect x="48" y="9" width="2" height="19"/><rect x="52" y="7" width="2" height="21"/><rect x="56" y="6" width="2" height="22"/>
        <rect x="60" y="7" width="2" height="21"/><rect x="64" y="10" width="2" height="18"/><rect x="68" y="14" width="2" height="14"/>
        <rect x="72" y="18" width="2" height="10"/><rect x="76" y="22" width="2" height="6"/>
      </g>
    </svg>
  </article>

  <section class="abs quotes">
    <h2 class="abs head quotes-title">What People are saying...</h2>
    <div class="abs quotes-rule"></div>
    <blockquote class="abs quote" style="left:28px">“My husband and I decided to go solar after 3 of our neighbors did. After having it I don't know why we waited so long!<span class="who">Marisa K.</span></blockquote>
    <blockquote class="abs quote" style="left:174px">“I had met with a few different companies and didn't care for their options. Our team had an option we liked and we went for it! Its been working great for us.<span class="who">Glen and Petra S.</span></blockquote>
    <blockquote class="abs quote" style="left:353px;width:164px">“We were a bit nervous to go solar.. after our consultation with Walt it was very easy to see that solar was our best option. Now we are saving tons on our electric bill! Thanks !<span class="who">Ron and Deb L.</span></blockquote>
  </section>

  <div class="abs photo" style="left:0;width:194px;background:linear-gradient(180deg,#cfd9e0 0%,#a5573e 45%,#8a4a36 70%,#6e9a3f 100%)" role="img" aria-label="Photo of a brick house with solar panels on the roof"></div>
  <div class="abs photo" style="left:197px;width:156px;background:linear-gradient(160deg,#2f4f8f 0%,#4a74b8 40%,#e4ddd0 70%,#c8c2b8 100%)" role="img" aria-label="Aerial photo of a flat roof covered in solar panels"></div>
  <div class="abs photo" style="left:356px;width:189px;background:linear-gradient(180deg,#b9c9d6 0%,#2e4a78 50%,#b4542e 80%,#7c3a24 100%)" role="img" aria-label="Photo of a tiled roof with solar panels and wind turbines behind"></div>
</section>

<!-- Page 2 -->
<section class="page page-right">
  <svg class="abs" style="left:0;top:0" width="547" height="430" viewBox="0 0 547 430" role="img" aria-label="Photo of a blue house with an orange tiled roof covered in solar panels">
    <defs>
      <linearGradient id="houseTone" x1="0" y1="0" x2="0" y2="1">
        <stop offset="0" stop-color="#dfe9f2"/>
        <stop offset=".35" stop-color="#3e5f8c"/>
        <stop offset=".6" stop-color="#4b7fb8"/>
        <stop offset=".85" stop-color="#5d8f3e"/>
        <stop offset="1" stop-color="#3f7a2a"/>
      </linearGradient>
    </defs>
    <path d="M0,140 C120,100 260,80 547,70 L547,250 C420,330 240,360 0,320 Z" fill="url(#houseTone)"/>
    <path d="M0,320 C240,360 420,330 547,250 L547,262 C420,345 240,375 0,333 Z" fill="var(--green)"/>
    <path d="M440,0 C510,40 540,110 547,170 L547,0 Z" fill="var(--blue)"/>
    <path d="M470,0 C520,30 543,80 547,120 L547,0 Z" fill="var(--green)"/>
    <path d="M500,0 C530,20 545,50 547,75 L547,0 Z" fill="#fff"/>
  </svg>

  <h1 class="abs title">SOLAR ENERGY</h1>
  <p class="abs head subtitle">$0 Upfront Cost</p>

  <div class="abs head badge">For<br>Military<br>base Housing<br>and other<br>Govt.<br>Projects</div>
  <div class="abs head logo">Corwick<br>Roof<br>Company</div>

  <h2 class="abs head easy">WE MAKE IT EASY</h2>

  <article class="abs step" style="left:27px;width:113px">
    <svg width="56" height="56" viewBox="0 0 56 56"><circle cx="28" cy="28" r="25" fill="#fff" stroke="#1a8fd6" stroke-width="3"/><rect x="17" y="19" width="22" height="14" fill="none" stroke="#1b75bb" stroke-width="2"/><rect x="13" y="34" width="30" height="3" fill="#1b75bb"/><circle cx="51" cy="26" r="4" fill="#8cc63f"/></svg>
    <h4>Speak to a solar consultant</h4>
    <p>Meet with one of our energy consultants to review your solar options.</p>
  </article>
  <article class="abs step" style="left:150px;width:106px">
    <svg width="56" height="56" viewBox="0 0 56 56"><circle cx="28" cy="28" r="25" fill="#fff" stroke="#1a8fd6" stroke-width="3"/><path d="M16,20 L40,20 L37,34 L19,34Z" fill="none" stroke="#1b75bb" stroke-width="2"/><line x1="28" y1="34" x2="28" y2="40" stroke="#1b75bb" stroke-width="2"/><circle cx="28" cy="52" r="4" fill="#8cc63f"/></svg>
    <h4>We'll design your solar panel system</h4>
    <p>We'll finalize the details for tip top accuracy.</p>
  </article>
  <article class="abs step" style="left:266px;width:113px">
    <svg width="56" height="56" viewBox="0 0 56 56"><circle cx="28" cy="28" r="25" fill="#fff" stroke="#8cc63f" stroke-width="3"/><rect x="18" y="16" width="16" height="22" fill="none" stroke="#1b75bb" stroke-width="2"/><circle cx="35" cy="35" r="6" fill="#fff" stroke="#1b75bb" stroke-width="2"/><circle cx="5" cy="26" r="4" fill="#8cc63f"/></svg>
    <h4>Schedule your 1 day install</h4>
    <p>Let us do the heavy lifting as you watch your home upgrade to solar.</p>
  </article>
  <article class="abs step" style="left:390px;width:128px">
    <svg width="56" height="56" viewBox="0 0 56 56"><circle cx="28" cy="28" r="25" fill="#fff" stroke="#8cc63f" stroke-width="3"/><circle cx="28" cy="25" r="8" fill="none" stroke="#8cc63f" stroke-width="2"/><rect x="24" y="34" width="8" height="5" fill="#8cc63f"/><circle cx="28" cy="4" r="4" fill="#8cc63f"/></svg>
    <h4>Start saving on your electricity bill</h4>
    <p>Watch your electric bill lower and your energy savings build for year to come.</p>
  </article>
  <svg class="abs" style="left:0;top:440px" width="547" height="30" viewBox="0 0 547 30" fill="none" stroke="#b9c2cc" stroke-width="1" stroke-dasharray="2 2">
    <path d="M120,12 Q135,20 150,8 M245,12 Q258,2 272,10 M370,12 Q385,20 398,8"/>
  </svg>

  <p class="abs head tagline">Bringing the Power of the SUN for you</p>
  <p class="abs head site">CorwickRoof.com</p>

  <svg class="abs" style="left:0;top:590px" width="547" height="117" viewBox="0 0 547 117">
    <polygon points="0,80 170,117 0,117" fill="var(--green)"/>
    <polygon points="150,117 547,0 547,117" fill="var(--blue)"/>
    <polygon points="140,117 547,-4 547,2 160,117" fill="#d8dde2"/>
  </svg>
  <p class="abs quote-cta" style="top:632px;font-size:13px;font-weight:600">Get a free quote</p>
  <p class="abs quote-cta" style="top:648px;font-size:24px;font-weight:600">(800) 555-0147</p>
  <p class="abs quote-cta" style="top:681px;font-size:10.5px;font-weight:500;color:#0d2f55">email: info@CorwickRoof.com</p>
</section>

</body>
</html>
```